New Zealand Luggage Importer Needs Business Cards

We need professional, creative and fashionable business cards created.
We are based in New Zealand and import and distribute high-end, quality, fashionable and durable luggage.
We pride ourselves on selling the very best quality luggage, second only to 1 brand (which we won't mention here)...we use the same manufacturer. However, our prices are much more reasonable.
Industry/Entity Type
Business
Contact Information for Business Card
Mark Dunsley
027 512 4068
3/17 Harlow Street, Pinecrest Flats, Auckland, 0614
PO Box 204377, Fernside, Auckland 0731
09-528-3916
sales@brivancases.co.nz / www.brivancases.co.nz

```html
<!DOCTYPE html>
<html lang="en">
<head>
<meta charset="utf-8">
<title>Brivan Cases – Business Card</title>
<link rel="stylesheet" href="https://fonts.googleapis.com/css2?family=Oswald:wght@500&family=Montserrat:wght@300;400;600&family=Great+Vibes&family=Open+Sans:wght@400&display=swap">
<style>
  :root {
    --bg: #ececec;
    --card-white: #ffffff;
    --card-grey: #f1f1f1;
    --ink: #111111;
    --black: #0c0c0c;
    --gold: #c9a64a;
    --photo-light: #e6e6e6;
    --photo-dark: #3a3a3a;
  }
  * { box-sizing: border-box; margin: 0; padding: 0; }
  html, body { width: 1200px; height: 800px; overflow: hidden; }
  body {
    background: var(--bg);
    font-family: "Open Sans", sans-serif;
    color: var(--ink);
    position: relative;
  }
  .card {
    position: absolute;
    width: 460px;
    height: 280px;
    overflow: hidden;
    box-shadow: 0 6px 18px rgba(0,0,0,0.12);
  }
  /* Cover */
  .card--cover {
    left: 90px; top: 260px;
    background: var(--black);
    display: flex; align-items: center; justify-content: center;
  }
  .brand-name {
    font-family: "Montserrat", sans-serif;
    font-weight: 600;
    letter-spacing: 0.12em;
    white-space: nowrap;
  }
  .card--cover .brand-name { color: #ffffff; font-size: 34px; }

  /* Inside spread */
  .spread { position: absolute; left: 650px; top: 120px; width: 460px; height: 560px; }
  .card--inside-top { left: 0; top: 0; background: var(--card-grey); box-shadow: none; }
  .card--inside-bottom { left: 0; top: 280px; background: var(--card-white); box-shadow: none; border-top: 1px solid #d8d8d8; }
  .spread { box-shadow: 0 6px 18px rgba(0,0,0,0.12); }

  .photo {
    position: absolute;
    background: linear-gradient(160deg, var(--photo-light) 0%, #9a9a9a 45%, var(--photo-dark) 100%);
  }
  .photo--top { left: 0; top: 60px; width: 250px; height: 220px; }
  .photo--bottom { left: 0; top: 0; width: 230px; height: 175px; }

  .tagline {
    position: absolute; right: 26px; top: 30px;
    text-align: right;
    font-family: "Oswald", sans-serif; font-weight: 500;
    color: var(--gold); text-transform: uppercase; line-height: 1.15;
  }
  .tagline__line1 { font-size: 17px; }
  .tagline__line2 { font-size: 23px; }
  .motto {
    position: absolute; right: 26px; top: 118px;
    font-family: "Montserrat", sans-serif; font-weight: 300;
    font-size: 21px; letter-spacing: 0.04em;
  }
  .motto__amp { font-family: "Great Vibes", cursive; font-size: 30px; padding: 0 4px; }

  .contact {
    position: absolute; right: 26px; top: 14px;
    text-align: right; font-size: 11.5px; line-height: 1.45;
  }
  .contact__name { font-family: "Great Vibes", cursive; font-size: 32px; line-height: 1.1; margin-bottom: 4px; }
  .contact__row { display: flex; justify-content: flex-end; align-items: center; gap: 6px; }
  .contact__row svg { width: 11px; height: 11px; fill: var(--ink); }
  .contact__address { margin-top: 4px; }

  .logo-strip {
    position: absolute; left: 0; right: 22px; bottom: 28px;
    display: flex; align-items: center; gap: 14px;
  }
  .logo-strip__bar { flex: 1; height: 22px; background: var(--black); }
  .logo-strip .brand-name { color: var(--ink); font-size: 28px; }
</style>
</head>
<body>

<section class="card card--cover" aria-label="Card cover">
  <span class="brand-name">BRIVAN CASES</span>
</section>

<section class="spread" aria-label="Card inside">
  <div class="card card--inside-top">
    <div class="photo photo--top" role="img" aria-label="Photo of black hard-shell suitcases, upper half"></div>
    <div class="tagline">
      <div class="tagline__line1">You've never experienced luggage</div>
      <div class="tagline__line2">Like this before !</div>
    </div>
    <div class="motto">STYLISH<span class="motto__amp">&amp;</span>ELEGANT</div>
  </div>

  <div class="card card--inside-bottom">
    <div class="photo photo--bottom" role="img" aria-label="Photo of black hard-shell suitcases on wheels, lower half"></div>
    <div class="contact">
      <div class="contact__name">Mark Dunsley</div>
      <div class="contact__row">027 512 4068
        <svg viewBox="0 0 24 24"><path d="M6.6 10.8a15 15 0 0 0 6.6 6.6l2.2-2.2c.3-.3.7-.4 1-.2 1.1.4 2.3.6 3.6.6.6 0 1 .4 1 1V20c0 .6-.4 1-1 1A17 17 0 0 1 3 4c0-.6.4-1 1-1h3.5c.6 0 1 .4 1 1 0 1.3.2 2.5.6 3.6.1.3 0 .7-.2 1z"/></svg></div>
      <div class="contact__row">09-528-3916
        <svg viewBox="0 0 24 24"><path d="M3 8c3-3 15-3 18 0v3h-5V9H8v2H3zm3 5h12l2 7H4z"/></svg></div>
      <div class="contact__row">sales@brivancases.co.nz
        <svg viewBox="0 0 24 24"><path d="M2 5h20v14H2zm2 2v.5l8 5 8-5V7z"/></svg></div>
      <div class="contact__row">www.brivancases.co.nz
        <svg viewBox="0 0 24 24"><circle cx="12" cy="12" r="9" fill="none" stroke="#111" stroke-width="2"/><path d="M3 12h18M12 3c3 3 3 15 0 18M12 3c-3 3-3 15 0 18" fill="none" stroke="#111" stroke-width="1.5"/></svg></div>
      <div class="contact__address">3/17 Harlow Street, Pinecrest Flats,<br>Auckland, 0614</div>
      <div>PO Box 204377, Fernside,<br>Auckland 0731</div>
    </div>
    <div class="logo-strip">
      <div class="logo-strip__bar"></div>
      <span class="brand-name">BRIVAN CASES</span>
    </div>
  </div>
</section>

</body>
</html>
```